Business Card Design Project

In addition to the logo design we want a professional and contemporary business card for a talent management agency. We provide management services to creative artists and want to communicate a professional creative vibe.
Updates

Reason: Sorry didnt realise I had put such a short timeline on it.

Target Market(s)

The business deals with creative artists and other industry professionals

Industry/Entity Type

Artists

Colors

Designer to choose colors to be used in the design.

Requirements
Must have
• Logo
Address
Phone
Email

```html
<!DOCTYPE html>
<html lang="en">
<head>
<meta charset="utf-8">
<title>Kestrel Talent — Business Card</title>
<link href="https://fonts.googleapis.com/css2?family=Montserrat:wght@400;600;800&display=swap" rel="stylesheet">
<style>
  :root {
    --green: #17583a;
    --black: #111111;
    --paper: #ffffff;
    --ink: #2b2b2b;
    --backdrop: #e9e6e1;
  }
  * { margin: 0; padding: 0; box-sizing: border-box; }
  html, body { width: 1200px; height: 960px; overflow: hidden; }
  body {
    background: var(--backdrop);
    font-family: "Montserrat", sans-serif;
    display: flex;
    flex-direction: column;
    align-items: center;
    justify-content: center;
    gap: 60px;
  }
  .card {
    position: relative;
    width: 600px;
    height: 340px;
    background: var(--paper);
    box-shadow: 0 6px 20px rgba(0,0,0,0.15);
    overflow: hidden;
  }
  .wordmark {
    color: var(--green);
    font-weight: 800;
    line-height: 0.95;
    letter-spacing: 0.02em;
    text-transform: uppercase;
  }
  /* Front */
  .card-front .wordmark {
    position: absolute;
    left: 40px;
    bottom: 44px;
    font-size: 44px;
  }
  .card-front .edge-band {
    position: absolute;
    top: 0; right: 0;
    width: 40px; height: 100%;
    background: var(--green);
  }
  .card-front .edge-rule {
    position: absolute;
    top: 0; right: 46px;
    width: 2px; height: 100%;
    background: var(--green);
  }
  /* Back */
  .card-back .swoosh { position: absolute; inset: 0; width: 100%; height: 100%; }
  .card-back .details {
    position: absolute;
    right: 34px;
    top: 34px;
    text-align: right;
  }
  .card-back .wordmark { font-size: 34px; }
  .person { margin-top: 26px; }
  .person-name { color: var(--green); font-weight: 600; font-size: 19px; }
  .person-role { color: var(--ink); font-size: 12px; margin-top: 2px; }
  .contacts { list-style: none; margin-top: 26px; font-size: 12px; color: var(--ink); line-height: 1.45; }
  .contacts li { display: flex; justify-content: flex-end; align-items: flex-start; gap: 10px; }
  .contacts svg { width: 14px; height: 14px; flex: none; margin-top: 2px; fill: var(--green); }
</style>
</head>
<body>

  <section class="card card-front" aria-label="Business card front">
    <div class="wordmark">Kestrel<br>Talent</div>
    <div class="edge-rule"></div>
    <div class="edge-band"></div>
  </section>

  <section class="card card-back" aria-label="Business card back">
    <svg class="swoosh" viewBox="0 0 600 340" preserveAspectRatio="none" aria-hidden="true">
      <path d="M0 0 H400 C300 60 230 160 215 340 H0 Z" fill="var(--green)"/>
      <path d="M382 26 C300 90 250 190 240 340 H226 C236 180 290 80 382 26 Z" fill="var(--black)"/>
    </svg>
    <div class="details">
      <div class="wordmark">Kestrel<br>Talent</div>
      <div class="person">
        <div class="person-name">Employee Name</div>
        <div class="person-role">Managing Director</div>
      </div>
      <ul class="contacts">
        <li><span>(+61 2) 9000 4417</span>
          <svg viewBox="0 0 16 16"><circle cx="8" cy="5" r="3.2"/><path d="M2 15c0-4 2.7-6 6-6s6 2 6 6z"/></svg></li>
        <li><span>hello@kestreltalent.com.au</span>
          <svg viewBox="0 0 16 16"><path d="M1 3h14v10H1z M2 4l6 5 6-5" fill="var(--green)"/><path d="M2 4.2l6 4.8 6-4.8" fill="none" stroke="#fff" stroke-width="1.2"/></svg></li>
        <li><span>14-18 Harbour Lane<br>Glenwood NSW 2011<br>Australia</span>
          <svg viewBox="0 0 16 16"><path d="M8 1l7 6.5h-2V15H9.5v-4h-3v4H3V7.5H1z"/></svg></li>
      </ul>
    </div>
  </section>

</body>
</html>
```